Varobel Profile Banner Design

Hi All

I would like to have a varobel profile banner design.
As I spend half my time between Zurich and Hong Kong I would like to have a Profile Banner that combines the two places.

Basic requirements:
- Image size: VaroBel banner or background photo size: 1584 x 396
- Feel: Professional but modern
- Make sure that there is nothing important that will be covered up by the varobel profile pic (left bottom)
- Should incorporate both cities (Hong Kong and Zurich)
- Text for Zurich part (city name): Zürich & (my name) "Tomas Engqvist"
- Text for Hong Kong part (City name): 香港 & (my name) "葉思恆"
- Should work well on mobile and web version of varobel

Please be creative and unique in your design.

Thanks

Tomas

Industry/Entity Type

Consulting, General business management

Requirements
Should not have
• No photo montages. Should be graphics

```html
<!DOCTYPE html>
<html lang="en">
<head>
<meta charset="utf-8">
<title>Zürich · 香港 Profile Banner</title>
<link rel="stylesheet" href="https://fonts.googleapis.com/css2?family=Libre+Baskerville&family=Open+Sans:wght@400&family=Noto+Sans+TC:wght@400&display=swap">
<style>
  :root {
    --stage: #ededed;
    --sky-top: #e6f2fa;
    --sky-mid: #f6fbfe;
    --navy: #10294a;
    --ink: #1b2f4c;
    --orange: #f07a1e;
    --magenta: #b8286d;
    --purple: #6b2f7e;
    --teal: #1c9c86;
    --red: #e0422c;
    --gold: #f5a623;
  }
  * { margin: 0; padding: 0; box-sizing: border-box; }
  html, body {
    width: 1200px;
    height: 904px;
    overflow: hidden;
    background: var(--stage);
  }
  .banner {
    position: absolute;
    left: 40px;
    top: 312px;
    width: 1120px;
    height: 280px;
    overflow: hidden;
    background: linear-gradient(90deg, var(--sky-top) 0%, var(--sky-mid) 45%, var(--sky-mid) 60%, var(--sky-top) 100%);
    box-shadow: 0 6px 18px rgba(0,0,0,0.18);
  }
  .banner-art {
    position: absolute;
    inset: 0;
    width: 1120px;
    height: 280px;
  }
  .city-label {
    position: absolute;
    color: var(--ink);
  }
  .city-label--zurich { left: 476px; top: 20px; }
  .city-label--hongkong { left: 681px; top: 18px; }
  .city-name-latin {
    font-family: "Libre Baskerville", Georgia, serif;
    font-size: 28px;
    line-height: 34px;
    letter-spacing: -0.5px;
  }
  .person-name-latin {
    font-family: "Open Sans", Arial, sans-serif;
    font-size: 15px;
    line-height: 20px;
    margin-left: 6px;
    letter-spacing: 0.2px;
  }
  .city-name-cjk {
    font-family: "Noto Sans TC", sans-serif;
    font-size: 28px;
    line-height: 34px;
    margin-left: 6px;
    letter-spacing: 1px;
  }
  .person-name-cjk {
    font-family: "Noto Sans TC", sans-serif;
    font-size: 16px;
    line-height: 22px;
    letter-spacing: 0.5px;
  }
</style>
</head>
<body>
  <section class="banner" aria-label="Zürich and Hong Kong profile banner">
    <svg class="banner-art" viewBox="0 0 1120 280" xmlns="http://www.w3.org/2000/svg">
      <defs>
        <linearGradient id="zurich-tones" x1="0" y1="0" x2="1" y2="0">
          <stop offset="0" stop-color="var(--orange)"/>
          <stop offset="0.2" stop-color="var(--magenta)"/>
          <stop offset="0.4" stop-color="var(--teal)"/>
          <stop offset="0.6" stop-color="var(--red)"/>
          <stop offset="0.8" stop-color="var(--purple)"/>
          <stop offset="1" stop-color="var(--orange)"/>
        </linearGradient>
        <linearGradient id="hongkong-tones" x1="0" y1="0" x2="1" y2="0">
          <stop offset="0" stop-color="var(--red)"/>
          <stop offset="0.2" stop-color="var(--gold)"/>
          <stop offset="0.4" stop-color="var(--teal)"/>
          <stop offset="0.6" stop-color="var(--magenta)"/>
          <stop offset="0.8" stop-color="var(--red)"/>
          <stop offset="1" stop-color="var(--teal)"/>
        </linearGradient>
      </defs>

      <polygon class="skyline skyline--zurich" role="img"
        aria-label="Colourful low-poly illustration of the Zürich skyline with Grossmünster towers, Fraumünster spire and old town houses"
        points="0,150 540,150 520,280 0,280" fill="url(#zurich-tones)"/>

      <polygon class="skyline skyline--hongkong" role="img"
        aria-label="Colourful low-poly illustration of the Hong Kong skyline with skyscrapers, a pagoda, the Big Buddha and a temple gate"
        points="610,120 1120,120 1120,280 566,280" fill="url(#hongkong-tones)"/>

      <polygon class="divider-band" points="636,0 656,0 558,280 538,280" fill="var(--navy)"/>
      <line class="divider-line" x1="662" y1="0" x2="605" y2="169" stroke="var(--navy)" stroke-width="1.2"/>
      <circle cx="605" cy="169" r="2.2" fill="var(--navy)"/>
      <line class="divider-line" x1="601" y1="99" x2="544" y2="280" stroke="var(--navy)" stroke-width="1.2"/>
      <circle cx="601" cy="99" r="2.2" fill="var(--navy)"/>
    </svg>

    <div class="city-label city-label--zurich">
      <div class="city-name-latin">ZÜRICH</div>
      <div class="person-name-latin">TOMAS ENGQVIST</div>
    </div>

    <div class="city-label city-label--hongkong">
      <div class="city-name-cjk">香港</div>
      <div class="person-name-cjk">葉思恆</div>
    </div>
  </section>
</body>
</html>
```